依頼詳細
完成見学会にて使用する【のぼり旗】のデザインを募集いたします。
600x1800のサイズで【月々5万円台から(~でも可)】【ZEH】【注文住宅専門店】の3つを分かりやすく目に入りやすいデザインで作成をお願いします。
それぞれのキーワードの前後に言葉を付け加えても、無くても結構です。
(例)月々5万円台からの注文住宅!、月々5万円台からのマイホーム!
高性能 ZEH!、省エネ×創エネ ZEH!
手が届く注文住宅!など

色合いとフォントは弊社のロゴマークに合うようにお願いします。
文字の配置や大きさ等は、添付データに沿ったデザインではなくて結構です。
記載項目
キャッチフレーズ、注文住宅専門店、ロゴマーク、そよみねホーム記載の検索窓イメージ

サイズ→600x1800
希望イメージ
シンプル 複雑
単色 カラフル
暗い 明るい
日常 高級
遊び心 厳粛
未来的 伝統的
女性的 男性的
希望する色
黄・オレンジ系、緑系、茶系、添付ロゴに沿った色合い
納品ファイル
• 高解像度JPG (.jpg)
• イラストレーター形式 (.ai)
• フォトショップ形式 (.psd)
• PNG形式 (.png)
補足説明
のぼり旗で使用するロゴデータを追記しました。
よろしくお願いします。
■ 選んだ理由

掲載して欲しいキーワードが分かりやすかったため選びました。
配色も社内で評判が良く、文字も見やすかったです。

■ 提案者全員のお礼・コメント

沢山のステキなご提案をありがとうございました。
また機会がありましたら宜しくお願いいたします。

```html
<!DOCTYPE html>
<html lang="ja">
<head>
<meta charset="utf-8">
<title>のぼり旗 そよみねホーム</title>
<link rel="stylesheet" href="https://fonts.googleapis.com/css2?family=M+PLUS+Rounded+1c:wght@700;800;900&family=Noto+Serif+JP:wght@500&display=swap">
<style>
  :root {
    --flag-brown: #a3825f;
    --panel-cream: #fdf6c9;
    --zeh-cream: #f6edb0;
    --ink-brown: #6a4627;
    --leaf-green: #8dc641;
    --white: #ffffff;
    --bar-dark: #3b3b3b;
    --mark-grey: #9a9a9a;
  }
  * { margin: 0; padding: 0; box-sizing: border-box; }
  html, body { width: 1200px; height: 2672px; overflow: hidden; background: var(--white); }
  body { position: relative; font-family: "M PLUS Rounded 1c", sans-serif; font-weight: 900; }
  .abs { position: absolute; white-space: nowrap; }

  .pole-marks { left: 0; top: 0; width: 1200px; height: 2672px; }

  .flag { left: 160px; top: 232px; width: 888px; height: 2216px; background: var(--flag-brown); }

  .tagline-energy { left: 160px; top: 356px; width: 888px; text-align: center; color: var(--white);
    font-weight: 900; font-size: 74px; line-height: 1; letter-spacing: 2px; }
  .tagline-zeh { left: 160px; top: 462px; width: 888px; text-align: center; color: var(--zeh-cream);
    font-family: "M PLUS Rounded 1c", sans-serif; font-weight: 900; font-size: 188px; line-height: 1; letter-spacing: 8px; }

  .panel { left: 288px; top: 660px; width: 728px; height: 1612px; background: var(--panel-cream); }

  .bubble { left: 700px; top: 668px; width: 200px; height: 160px; }
  .bubble-text { left: 716px; top: 700px; width: 176px; text-align: center; color: var(--white);
    font-weight: 900; font-size: 68px; line-height: 1; }

  .price-number { left: 346px; top: 740px; color: var(--ink-brown); font-weight: 900;
    font-size: 440px; line-height: 1; }
  .price-unit { left: 660px; top: 920px; color: var(--ink-brown); font-weight: 900;
    font-size: 88px; line-height: 1.2; }

  .catch-line { left: 288px; width: 728px; text-align: center; color: var(--ink-brown);
    font-weight: 900; line-height: 1; }
  .catch-reach { top: 1200px; font-size: 116px; }
  .catch-house { top: 1360px; font-size: 124px; letter-spacing: 4px; }

  .illustration { left: 360px; top: 1560px; width: 560px; height: 320px; border-radius: 40px;
    background: radial-gradient(ellipse at 50% 55%, #b9c9e6 0%, #d8e4c4 55%, var(--panel-cream) 80%); }

  .shop-pill { left: 336px; top: 1988px; width: 624px; height: 88px; border-radius: 44px;
    background: var(--leaf-green); color: var(--white); text-align: center;
    font-weight: 800; font-size: 58px; line-height: 88px; }

  .brand { left: 350px; top: 2126px; width: 620px; height: 110px; display: flex; align-items: center; gap: 20px; }
  .brand-square { width: 64px; height: 64px; background: var(--leaf-green); flex: none; }
  .brand-name { color: var(--ink-brown); font-weight: 800; font-size: 70px; line-height: 1; white-space: nowrap; }

  .search-box { left: 344px; top: 2312px; width: 640px; height: 76px; background: var(--white);
    border: 4px solid var(--bar-dark); display: flex; align-items: center; }
  .search-text { flex: 1; padding-left: 18px; font-family: "Noto Serif JP", serif; font-weight: 500;
    font-size: 46px; color: #222; line-height: 1; white-space: nowrap; }
  .search-button { width: 130px; height: 100%; background: var(--bar-dark); display: flex;
    align-items: center; justify-content: center; }
  .cursor { left: 820px; top: 2352px; width: 72px; height: 84px; }
</style>
</head>
<body>

<svg class="abs pole-marks" viewBox="0 0 1200 2672" aria-hidden="true">
  <g fill="none" stroke="var(--mark-grey)" stroke-width="3">
    <line x1="160" y1="232" x2="160" y2="2448"/>
    <line x1="160" y1="232" x2="1048" y2="232"/>
  </g>
  <g fill="#fff" stroke="var(--mark-grey)" stroke-width="3">
    <g id="ring">
      <rect x="-22" y="-22" width="44" height="44"/>
      <line x1="-22" y1="-22" x2="22" y2="22"/>
      <line x1="22" y1="-22" x2="-22" y2="22"/>
    </g>
    <use href="#ring" x="160" y="196"/>
    <use href="#ring" x="600" y="196"/>
    <use href="#ring" x="1048" y="196"/>
    <use href="#ring" x="160" y="296"/>
    <use href="#ring" x="1048" y="296"/>
    <use href="#ring" x="160" y="820"/>
    <use href="#ring" x="160" y="1360"/>
    <use href="#ring" x="160" y="1880"/>
    <use href="#ring" x="160" y="2420"/>
  </g>
</svg>

<div class="abs flag"></div>

<p class="abs tagline-energy">省エネ × 創エネ</p>
<p class="abs tagline-zeh">ZEH</p>

<div class="abs panel"></div>

<svg class="abs bubble" viewBox="0 0 200 160" aria-hidden="true">
  <path d="M110 8 C158 8 194 36 194 72 C194 108 158 134 110 134 C96 134 84 132 72 128 L28 150 L46 114 C26 102 18 88 18 72 C18 36 60 8 110 8 Z" fill="var(--leaf-green)"/>
</svg>
<p class="abs bubble-text">月々</p>

<p class="abs price-number">5</p>
<p class="abs price-unit">万円<br>～の</p>

<p class="abs catch-line catch-reach">手が届く！</p>
<p class="abs catch-line catch-house">注文住宅</p>

<div class="abs illustration" role="img" aria-label="家の前に立つ家族のイラスト"></div>

<p class="abs shop-pill">注文住宅専門店</p>

<div class="abs brand">
  <span class="brand-square"></span>
  <span class="brand-name">そよみねホーム</span>
</div>

<div class="abs search-box">
  <span class="search-text">そよみねホーム</span>
  <span class="search-button">
    <svg width="46" height="46" viewBox="0 0 50 50" aria-hidden="true">
      <circle cx="20" cy="20" r="13" fill="none" stroke="#fff" stroke-width="5"/>
      <line x1="30" y1="30" x2="44" y2="44" stroke="#fff" stroke-width="6" stroke-linecap="round"/>
    </svg>
  </span>
</div>

<svg class="abs cursor" viewBox="0 0 80 90" aria-hidden="true">
  <path d="M6 4 L6 70 L22 56 L34 84 L46 78 L34 52 L56 52 Z" fill="#fff" stroke="#222" stroke-width="4" stroke-linejoin="round"/>
</svg>

</body>
</html>
```